Agriculture new feeding concept for bull fattening needs a one-page flyer *

We are the innovation leader in the field of cattle feeding in Switzerland. Now we are launching a new “Tarsela” project for cattle fatteners, Munimäster (bull fattening). Tarsela is a complete fattening regime (feed, feed additives, services and advice).
Our sales representatives are with customers every day. You advertise the new project with the aim that our internal specialists get an appointment with the customer for a non-binding presentation of the project. This flyer is intended for this purpose.
Effect:
1. Innovative, modern
2. New
3. emotions
4. technical, scientific

You are also welcome to create a “logo” for Tarsela or choose / design your own lettering.
If you wish to use them, you will also find pictures of such fattening bulls in the appendix. However, pictures are not absolutely necessary.
Size A5, one-sided
Title: TARSELA - for beef fattening professionals
Text:
• Best fattening results
• Top customer service
• Innovative products
• Attractive conditions

Banner or similar:
May we introduce ourselves? or we would be happy to visit you. Etc.

```html
<!DOCTYPE html>
<html lang="en">
<head>
<meta charset="utf-8">
<title>Tarsela – for beef fattening professionals</title>
<link href="https://fonts.googleapis.com/css2?family=Open+Sans:wght@300;400;600;700;800&display=swap" rel="stylesheet">
<style>
  :root {
    --page: #e9ebee;
    --slate: #95a6b8;
    --yellow: #e2bd00;
    --ink: #1b2633;
    --white: #ffffff;
    --hide-brown: #8a4a24;
    --hide-cream: #e8dccb;
  }
  html, body {
    margin: 0;
    width: 973px;
    height: 1200px;
    overflow: hidden;
    background: var(--page);
    font-family: "Open Sans", sans-serif;
  }
  .flyer {
    position: absolute;
    left: 63px;
    top: 0;
    width: 1072px;
    height: 1521px;
    transform: scale(0.789);
    transform-origin: 0 0;
    background: var(--slate);
    overflow: hidden;
    color: var(--ink);
    white-space: nowrap;
  }
  .shapes { position: absolute; inset: 0; }
  .headline {
    position: absolute;
    left: 70px;
    top: 212px;
    padding-left: 26px;
    border-left: 2px solid var(--ink);
    line-height: 1.18;
  }
  .headline .brand {
    font-size: 56px;
    font-weight: 800;
    letter-spacing: 0.5px;
    margin: 0 0 6px;
  }
  .headline .tagline {
    font-size: 36px;
    font-weight: 300;
    margin: 0;
  }
  .headline .tagline strong { font-weight: 700; }
  .brand-mark {
    position: absolute;
    left: 700px;
    top: 228px;
    width: 290px;
    text-align: center;
    font-size: 50px;
    font-weight: 800;
    letter-spacing: 5px;
    color: var(--ink);
  }
  .benefits {
    position: absolute;
    left: 134px;
    top: 1078px;
    margin: 0;
    padding: 0;
    list-style: none;
    font-size: 33px;
    font-weight: 600;
  }
  .benefits li {
    display: flex;
    align-items: center;
    height: 49px;
  }
  .benefits svg { width: 28px; height: 28px; margin-right: 12px; flex: none; }
  .intro-banner {
    position: absolute;
    left: 141px;
    top: 1337px;
    width: 790px;
    height: 70px;
    background: var(--white);
    border-radius: 14px 14px 0 0;
    text-align: center;
    font-size: 39px;
    font-weight: 700;
    line-height: 74px;
  }
  .contact-bar {
    position: absolute;
    left: 71px;
    top: 1405px;
    width: 930px;
    height: 69px;
    background: var(--yellow);
    border-radius: 12px;
    display: flex;
    align-items: center;
    font-size: 41px;
    font-weight: 700;
    line-height: 1;
  }
  .contact-bar .item { display: flex; align-items: center; white-space: nowrap; flex: none; }
  .contact-bar .phone { margin-left: 48px; }
  .contact-bar svg { margin-right: 12px; flex: none; }
  .contact-bar .divider {
    width: 2px;
    height: 34px;
    background: var(--ink);
    margin: 0 40px 0 42px;
    flex: none;
  }
</style>
</head>
<body>
<main class="flyer">
  <svg class="shapes" viewBox="0 0 1072 1521" width="1072" height="1521">
    <defs>
      <linearGradient id="herd" x1="0" y1="0" x2="1" y2="1">
        <stop offset="0" stop-color="#6e3519"/>
        <stop offset="0.35" stop-color="var(--hide-brown)"/>
        <stop offset="0.6" stop-color="#c9a27f"/>
        <stop offset="1" stop-color="var(--hide-cream)"/>
      </linearGradient>
    </defs>
    <path class="title-panel" fill="var(--yellow)"
          d="M0,150 Q0,68 135,68 Q170,68 205,86 L540,280 L0,585 Z"/>
    <rect class="benefit-panel" fill="var(--yellow)" x="96" y="760" width="485" height="542" rx="20"/>
    <path class="herd-photo" role="img" aria-label="Photo of young Hereford fattening bulls at a feed barrier"
          fill="url(#herd)"
          d="M540,280 L1072,587 L1072,1160 Q1072,1290 960,1262 L96,807 L30,770 Q-20,690 30,630 Z"/>
  </svg>

  <header class="headline">
    <h1 class="brand">TARSELA</h1>
    <p class="tagline">for beef <strong>fattening<br>professionals</strong></p>
  </header>

  <div class="brand-mark">TARSELA</div>

  <ul class="benefits">
    <li><svg viewBox="0 0 28 28"><circle cx="14" cy="14" r="12" fill="none" stroke="currentColor" stroke-width="2"/><path d="M8.5 14.5l4 4 7-8" fill="none" stroke="currentColor" stroke-width="2"/></svg>Best Fattening Results</li>
    <li><svg viewBox="0 0 28 28"><circle cx="14" cy="14" r="12" fill="none" stroke="currentColor" stroke-width="2"/><path d="M8.5 14.5l4 4 7-8" fill="none" stroke="currentColor" stroke-width="2"/></svg>Top Customer Service</li>
    <li><svg viewBox="0 0 28 28"><circle cx="14" cy="14" r="12" fill="none" stroke="currentColor" stroke-width="2"/><path d="M8.5 14.5l4 4 7-8" fill="none" stroke="currentColor" stroke-width="2"/></svg>Innovative Products</li>
    <li><svg viewBox="0 0 28 28"><circle cx="14" cy="14" r="12" fill="none" stroke="currentColor" stroke-width="2"/><path d="M8.5 14.5l4 4 7-8" fill="none" stroke="currentColor" stroke-width="2"/></svg>Attractive Conditions</li>
  </ul>

  <div class="intro-banner">MAY WE INTRODUCE OURSELVES?</div>

  <div class="contact-bar">
    <span class="item phone">
      <svg width="36" height="36" viewBox="0 0 36 36"><circle cx="18" cy="18" r="16" fill="none" stroke="var(--ink)" stroke-width="2"/><path d="M12 10c2-1 3 0 4 3s-2 3-1 5 3 4 5 4 2-3 5-1 2 3 1 4c-3 3-9 1-13-4s-4-10-1-11z" fill="none" stroke="var(--ink)" stroke-width="2"/></svg>
      0123 987 654
    </span>
    <span class="divider"></span>
    <span class="item email">
      <svg width="38" height="28" viewBox="0 0 38 28"><rect x="1" y="1" width="36" height="26" fill="none" stroke="var(--ink)" stroke-width="2"/><path d="M1 1l18 15L37 1M1 27l13-12M37 27L24 15" fill="none" stroke="var(--ink)" stroke-width="2"/></svg>
      hello@tarsela.com
    </span>
  </div>
</main>
</body>
</html>
```